Design a Website Mockup for VIP Taxi Transfers

Design website mockup for website providing Taxi Transfers (mainly airports transfers).
Company is specialized in Aurevia Transfers and website will be only VIP oriented.

As an example you can have a look at: http://www.pexora-worldwide.example/
We need more trendy design than Pexora Worldwide, but the main point is that the design must say (show) that it is Aurevia Transfers for VIP persons and not ordinary people. So everything must be in luxury format.
1. As a name for the company you can take "Aurevia Transfers" and some dummy slogan (it doesn't matter in this point)
2. We will need simple logo with website mockup
3. Website will be responsive, so you can take that in account
4. The most important message of the design must be "LUXURY", it must be simple and luxurious.
5. Show us two-three pages of the website (e.g. Homepage, Fleet (cars) page, Contact us page, Vobrel Spots page with custom markers (locations where we work).
6. We only need PSD files.

If you will have any further question or clarification, don't hesitate to ask them.
Good Luck!!!

```html
<!DOCTYPE html>
<html lang="en">
<head>
<meta charset="utf-8">
<title>Aurevia Transfers – Contact Us</title>
<link href="https://fonts.googleapis.com/css2?family=Tinos:ital,wght@0,400;0,700;1,400;1,700&display=swap" rel="stylesheet">
<style>
  :root {
    --bg-edge: #5e2818;
    --bg-mid: #7a3a24;
    --bg-glow: #a8613f;
    --gold: #f0cf8a;
    --gold-deep: #c4913f;
    --rule: #3e180d;
    --field: #2e130b;
    --field-border: #8a5535;
    --map-dark: #3d3a2f;
    --map-light: #8c8878;
  }
  * { box-sizing: border-box; margin: 0; padding: 0; }
  html, body { width: 1200px; height: 561px; overflow: hidden; }
  body {
    position: relative;
    font-family: "Tinos", "Times New Roman", serif;
    color: var(--gold);
    background:
      radial-gradient(ellipse 520px 360px at 390px 270px, var(--bg-glow) 0%, var(--bg-mid) 55%, transparent 100%),
      var(--bg-edge);
  }
  .rule { position: absolute; height: 1px; background: var(--rule); box-shadow: 0 1px 0 rgba(240,207,138,0.12); }
  .rule--top { left: 264px; width: 675px; top: 27px; }
  .rule--nav { left: 240px; width: 723px; top: 76px; }
  .rule--footer { left: 340px; width: 513px; top: 504px; }
  .top-knot {
    position: absolute; left: 596px; top: 18px; width: 9px; height: 9px;
    border: 1px solid var(--gold-deep); border-radius: 50%;
  }
  .site-nav a {
    position: absolute; top: 44px; font-size: 13px; color: var(--gold);
    text-decoration: none;
  }
  .brand {
    position: absolute; left: 512px; top: 42px; font-size: 17px;
    color: var(--gold-deep); display: flex; align-items: center; gap: 8px;
    white-space: nowrap;
  }
  .brand-dot { width: 9px; height: 9px; border-radius: 50%; background: var(--gold-deep); }
  .page-title {
    position: absolute; left: 241px; top: 129px; font-size: 21px;
    font-style: italic; font-weight: 700;
  }
  .field-label {
    position: absolute; left: 241px; font-size: 12px; font-style: italic; font-weight: 700;
  }
  .field {
    position: absolute; left: 240px; width: 288px;
    background: var(--field); border: 1px solid var(--field-border); border-radius: 3px;
    box-shadow: inset 0 2px 4px rgba(0,0,0,0.5);
  }
  .send {
    position: absolute; left: 240px; top: 424px; width: 57px; height: 25px;
    border-radius: 3px; border: 1px solid #8a6020;
    background: linear-gradient(#f3cf78, #c48c30);
    color: #3a1a0a; font: italic 700 14px "Tinos", serif;
  }
  .map {
    position: absolute; left: 580px; top: 195px; width: 380px; height: 220px;
    background: linear-gradient(90deg, var(--map-light) 0%, #7b7667 55%, var(--map-dark) 70%, #2f2e24 100%);
  }
  .copyright {
    position: absolute; top: 522px; left: 0; width: 1200px; text-align: center;
    font-size: 9px;
  }
</style>
</head>
<body>
  <div class="rule rule--top"></div>
  <div class="top-knot"></div>
  <nav class="site-nav">
    <a href="#" style="left:362px">Home</a>
    <a href="#" style="left:415px">About</a>
    <a href="#" style="left:741px">Book</a>
    <a href="#" style="left:792px">Contact</a>
  </nav>
  <div class="brand"><span>Aurevia Transfers</span><span class="brand-dot"></span></div>
  <div class="rule rule--nav"></div>

  <h1 class="page-title">Contact Us</h1>

  <form>
    <label class="field-label" style="top:185px">Name</label>
    <div class="field" style="top:203px;height:32px"></div>
    <label class="field-label" style="top:257px">Email</label>
    <div class="field" style="top:276px;height:32px"></div>
    <label class="field-label" style="top:329px">Message</label>
    <div class="field" style="top:347px;height:62px"></div>
    <button class="send" type="button">SEND</button>
  </form>

  <div class="map" role="img" aria-label="Satellite map showing the company location"></div>

  <div class="rule rule--footer"></div>
  <p class="copyright">Copyright © Aurevia Transfer 2013. All Rights Reserved.</p>
</body>
</html>
```